Pup Snack Den - New Website Design

Create a professional Vendrella website for a the hottest trend; a Pup Snack Den subscription box business. Vendrella.com is an easy to use website builder.
Please see frillomix.example; sweetorbit.example and wagcrate.example for the concept I am after. The business has not been launched yet, I am currently in the pre-launch stage using a specialized landing page website, and so the time scale for developing my professional looking Vendrella website is up to 1-2 weeks.
The webpage should have a fun feel and should match the style of the company logo at sweetorbit.example. The pages to include are 'Home', 'About us' and 'Get Started'
Thank you and good luck!

```html
<!DOCTYPE html>
<html lang="en">
<head>
<meta charset="utf-8">
<title>Pup Snack Den</title>
<link href="https://fonts.googleapis.com/css2?family=Raleway:wght@500;600;700;800&family=Open+Sans:wght@400;600;700&display=swap" rel="stylesheet">
<style>
:root{
  --orange:#f7a71c;
  --orange-dark:#e8940a;
  --ink:#222222;
  --text:#555555;
  --muted:#8a8a8a;
  --line:#e6e6e6;
  --blue:#3a7fbf;
  --footer:#1f1f1f;
  --white:#ffffff;
}
*{margin:0;padding:0;box-sizing:border-box}
html,body{width:1200px;height:4167px;overflow:hidden;background:var(--white)}
body{font-family:"Open Sans",Arial,sans-serif;color:var(--text);position:relative}
.abs{position:absolute}

/* header */
.header{position:absolute;top:0;left:0;width:1200px;height:200px;background:var(--orange)}
.logo{position:absolute;left:97px;top:36px;display:flex;align-items:center;gap:14px;color:var(--white);font-family:"Raleway",sans-serif;font-weight:800;font-size:30px;letter-spacing:1px}
.logo-dot{width:44px;height:44px;border-radius:50%;background:var(--white)}
.search{position:absolute;left:403px;top:42px;width:494px;height:44px;background:var(--white);display:flex}
.search span{flex:1;padding:12px 16px;font-size:13px;color:var(--muted)}
.search b{width:48px;background:var(--blue);display:flex;align-items:center;justify-content:center}
.account{position:absolute;top:30px;width:80px;text-align:center;color:var(--white);font-size:12px;font-weight:700;text-transform:uppercase}
.account i{display:flex;margin:0 auto 8px;width:42px;height:42px;border-radius:50%;background:var(--white);align-items:center;justify-content:center}
.nav{position:absolute;top:160px;left:97px;display:flex;font-size:13px;font-weight:700;color:var(--white);text-transform:uppercase}
.nav a{margin-right:44px;color:inherit;text-decoration:none}
.call{position:absolute;top:158px;right:97px;color:var(--white);font-weight:700;font-size:15px;display:flex;gap:10px;align-items:center}

/* features */
.features{position:absolute;top:200px;left:0;width:1200px;height:78px;border-bottom:1px solid var(--line)}
.feature{position:absolute;top:28px;display:flex;align-items:center;gap:12px;font-size:13px;color:var(--muted)}
.feature strong{color:var(--ink);font-weight:700;text-transform:uppercase}

/* hero */
.hero{position:absolute;top:278px;left:0;width:1200px;height:458px;background:linear-gradient(100deg,#c9b59a 0%,#a88a6a 40%,#6e5a48 70%,#3e3026 100%)}
.hero-title{position:absolute;top:398px;width:1200px;text-align:center;font-family:"Raleway",sans-serif;font-weight:800;font-size:72px;color:var(--white);letter-spacing:1px}
.hero-sub{position:absolute;top:488px;width:1200px;text-align:center;font-family:"Raleway",sans-serif;font-weight:600;font-size:40px;color:var(--white);text-transform:uppercase}
.btn{display:inline-block;background:var(--orange);color:var(--white);font-weight:700;font-size:13px;text-transform:uppercase;border-radius:22px}
.hero-btn{position:absolute;top:565px;left:522px;width:156px;height:44px;line-height:44px;text-align:center}
.dots{position:absolute;top:684px;left:550px;display:flex;gap:8px}
.dots i{width:14px;height:14px;border-radius:50%;border:2px solid var(--white)}
.dots i.on{background:var(--white)}
.arrow{position:absolute;top:490px;width:34px;height:34px;border-radius:50%;background:rgba(255,255,255,.35);display:flex;align-items:center;justify-content:center}

/* section titles */
.center-title{position:absolute;width:1200px;text-align:center;font-family:"Raleway",sans-serif;font-weight:700;font-size:34px;color:var(--ink);text-transform:uppercase}
.about-text{position:absolute;top:870px;left:190px;width:820px;text-align:center;font-size:13px;line-height:30px;color:var(--muted)}
.sec-title{position:absolute;left:97px;font-family:"Raleway",sans-serif;font-weight:700;font-size:34px;color:var(--ink);text-transform:uppercase}
.sec-title::after{content:"";position:absolute;left:0;bottom:-14px;width:54px;height:3px;background:var(--orange)}

/* gallery tiles */
.tile{position:absolute;overflow:hidden}
.tile .ph{position:absolute;inset:0}
.tag{position:absolute;left:18px;bottom:18px;background:var(--white);padding:14px 18px;min-width:160px}
.tag h4{font-size:15px;font-weight:600;color:var(--ink);text-transform:uppercase}
.tag p{font-size:15px;color:var(--orange);font-weight:600;margin-top:6px}

/* products */
.card{position:absolute;width:234px;height:252px;border:1px solid var(--line)}
.card .ph{position:absolute;left:40px;top:30px;width:154px;height:150px;border-radius:6px}
.new{position:absolute;left:0;top:0;width:0;height:0;border-top:76px solid var(--blue);border-right:76px solid transparent}
.new span{position:absolute;left:6px;top:-64px;transform:rotate(-45deg);color:var(--white);font-size:11px;font-weight:700}
.icons{position:absolute;bottom:16px;left:77px;display:flex;gap:6px}
.icons i{width:24px;height:24px;border:1px solid var(--line)}
.pinfo{position:absolute;width:234px;text-align:center}
.pinfo h5{font-size:15px;font-weight:700;color:var(--ink);text-transform:uppercase}
.pinfo p{font-size:15px;color:var(--orange);font-weight:600;margin-top:14px}
.stars{margin-top:6px;color:var(--orange);font-size:16px;letter-spacing:3px}

/* newsletter */
.news-band{position:absolute;top:2736px;left:0;width:1200px;height:292px;background:linear-gradient(90deg,#b7a18a,#d7c8b6 45%,#9b8874)}
.news-panel{position:absolute;top:2736px;left:247px;width:706px;height:292px;background:rgba(110,110,110,.55)}
.news-title{position:absolute;top:62px;left:0;width:706px;text-align:center;font-family:"Raleway",sans-serif;font-weight:700;font-size:30px;color:var(--white);text-transform:uppercase}
.news-text{position:absolute;top:124px;left:20px;width:666px;text-align:center;font-size:12px;color:#f0f0f0}
.news-input{position:absolute;top:182px;left:0;width:556px;height:50px;background:var(--white);padding:15px 20px;font-size:13px;color:var(--muted)}
.news-btn{position:absolute;top:182px;left:564px;width:142px;height:50px;line-height:50px;text-align:center;border-radius:0}

/* blog */
.post{position:absolute;top:3208px;width:322px;height:459px;border:1px solid var(--line)}
.post .ph{height:237px}
.post .body{padding:20px 16px}
.date{font-size:12px;color:var(--muted)}
.post h5{font-size:14px;font-weight:700;color:var(--ink);text-transform:uppercase;margin:14px 0 12px}
.post p{font-size:12px;line-height:20px;color:var(--muted)}
.more{display:block;margin-top:12px;font-size:12px;color:var(--orange)}

/* footer */
.footer{position:absolute;top:3750px;left:0;width:1200px;height:417px;background:var(--footer);color:#d0d0d0;font-size:13px}
.fcol{position:absolute;top:78px}
.fcol h6{font-size:15px;font-weight:700;color:var(--white);text-transform:uppercase;text-decoration:underline;margin-bottom:22px}
.fcol li{list-style:none;margin-bottom:16px;display:flex;gap:12px;align-items:flex-start}
.fcol li::before{content:"";margin-top:5px;width:0;height:0;border-left:6px solid #cfcfcf;border-top:4px solid transparent;border-bottom:4px solid transparent;flex:none}
.fcol.contact li::before{display:none}
.social{display:flex;gap:12px}
.social i{width:34px;height:34px;border:2px solid var(--white);border-radius:50%}
.fbottom{position:absolute;top:368px;left:97px;width:1006px;display:flex;justify-content:space-between;align-items:center;font-size:12px}
.pay{display:flex;gap:6px}
.pay i{width:30px;height:20px;background:#e6e6e6;border-radius:2px}
</style>
</head>
<body>

<header class="header">
  <div class="logo"><span class="logo-dot"></span>Pup Snack Den</div>
  <div class="search"><span>Search...</span><b><svg width="18" height="18" viewBox="0 0 18 18"><circle cx="7.5" cy="7.5" r="5.5" fill="none" stroke="#fff" stroke-width="2"/><line x1="11.5" y1="11.5" x2="16" y2="16" stroke="#fff" stroke-width="2"/></svg></b></div>
  <div class="account" style="left:946px"><i><svg width="20" height="20" viewBox="0 0 20 20"><circle cx="10" cy="7" r="4" fill="#f7a71c"/><path d="M3 18c1-4 4-6 7-6s6 2 7 6z" fill="#f7a71c"/></svg></i>Sign In</div>
  <div class="account" style="left:1030px"><i><svg width="20" height="20" viewBox="0 0 20 20"><path d="M2 3h3l2 10h9l2-7H6" fill="none" stroke="#f7a71c" stroke-width="2"/><circle cx="8" cy="17" r="1.5" fill="#f7a71c"/><circle cx="15" cy="17" r="1.5" fill="#f7a71c"/></svg></i>My Cart</div>
  <nav class="nav"><a>Home</a><a>About Us</a><a>Products</a><a>Blog</a><a>Contact Us</a></nav>
  <div class="call"><svg width="16" height="16" viewBox="0 0 16 16"><path d="M3 1l3 3-2 2c1 2 3 4 5 5l2-2 3 3-2 3C7 15 1 9 1 3z" fill="#fff"/></svg>CALL US : (555) - 014 - 2290</div>
</header>

<section class="features">
  <div class="feature" style="left:120px"><svg width="26" height="18" viewBox="0 0 26 18"><rect x="1" y="2" width="15" height="11" fill="#333"/><path d="M16 6h5l4 4v3h-9z" fill="#333"/><circle cx="6" cy="15" r="2.5" fill="#333"/><circle cx="20" cy="15" r="2.5" fill="#333"/></svg><strong>Free Shipping</strong> - Lorem ipsum dolor</div>
  <div class="feature" style="left:445px"><svg width="22" height="22" viewBox="0 0 22 22"><path d="M4 11a7 7 0 0 1 12-5M18 11a7 7 0 0 1-12 5" fill="none" stroke="#333" stroke-width="2"/><path d="M16 2v5h-5M6 20v-5h5" fill="none" stroke="#333" stroke-width="2"/></svg><strong>Money Back Guarantee</strong> - Nulla porta</div>
  <div class="feature" style="left:805px"><svg width="22" height="22" viewBox="0 0 22 22"><circle cx="11" cy="11" r="9" fill="none" stroke="#333" stroke-width="2"/><path d="M11 6v5l3 3" fill="none" stroke="#333" stroke-width="2"/></svg><strong>24/7 Support</strong> - Always here for you</div>
</section>

<section class="hero" role="img" aria-label="Photo of a toddler feeding treats to a brown puppy on a wooden floor"></section>
<div class="arrow" style="left:48px"><svg width="10" height="14" viewBox="0 0 10 14"><path d="M8 1L2 7l6 6" fill="none" stroke="#fff" stroke-width="2"/></svg></div>
<div class="arrow" style="left:1118px"><svg width="10" height="14" viewBox="0 0 10 14"><path d="M2 1l6 6-6 6" fill="none" stroke="#fff" stroke-width="2"/></svg></div>
<h1 class="hero-title">PUP SNACK DEN</h1>
<p class="hero-sub">Subscription Box Business</p>
<span class="btn hero-btn">Read More</span>
<div class="dots"><i class="on"></i><i></i><i></i><i></i><i></i></div>

<h2 class="center-title" style="top:808px">About Pup Snack Den</h2>
<p class="about-text">Every month we pack a box of tasty, wholesome snacks and fun chews for your pup, picked by our team and delivered right to your door so tails keep wagging all month long. Fresh treats, new toys and happy dogs, every single time.</p>

<div class="tile" style="left:97px;top:978px;width:611px;height:361px"><div class="ph" role="img" aria-label="Photo of a dog sniffing into a cardboard box" style="background:linear-gradient(120deg,#f3e2b8,#d9a968)"></div><div class="tag"><h4>Harum Quidem</h4><p>$52.28</p></div></div>
<div class="tile" style="left:97px;top:1347px;width:611px;height:361px"><div class="ph" role="img" aria-label="Photo of a white puppy lying on a rug" style="background:linear-gradient(120deg,#e8e4de,#c7bdb2)"></div><div class="tag"><h4>Maxime Placea</h4><p>$52.28</p></div></div>
<div class="tile" style="left:717px;top:978px;width:383px;height:236px"><div class="ph" role="img" aria-label="Photo of a cat and dog eating from a green bowl" style="background:linear-gradient(120deg,#e2ded8,#a89c90)"></div><div class="tag"><h4>Omnis Voluptas</h4><p>$52.28</p></div></div>
<div class="tile" style="left:717px;top:1225px;width:383px;height:236px"><div class="ph" role="img" aria-label="Photo of jars of bone-shaped biscuits" style="background:linear-gradient(120deg,#d9b98a,#8a6a4a)"></div><div class="tag"><h4>Soluta Nobis</h4><p>$52.28</p></div></div>
<div class="tile" style="left:717px;top:1472px;width:383px;height:236px"><div class="ph" role="img" aria-label="Photo of plush dog toys on a striped blanket" style="background:linear-gradient(120deg,#c9a97a,#7a4a4a)"></div><div class="tag"><h4>Soluta Nobis</h4><p>$52.28</p></div></div>

<h2 class="sec-title" style="top:1778px">Our Products</h2>
<div class="abs" role="img" aria-label="Photo of a small dog with large ears" style="left:917px;top:1736px;width:140px;height:150px;background:radial-gradient(circle,#d8c6b0,#ffffff 70%)"></div>

<div class="card" style="left:97px;top:1886px"><div class="ph" role="img" aria-label="Blue bowl of dry dog food" style="background:radial-gradient(circle,#8a5a3a,#6fc3e0)"></div><div class="new"><span>NEW</span></div><div class="icons"><i></i><i></i><i></i></div></div>
<div class="card" style="left:356px;top:1886px"><div class="ph" role="img" aria-label="Bag of jerky treats" style="background:radial-gradient(circle,#c47a3a,#f2e2cc)"></div><div class="icons"><i></i><i></i><i></i></div></div>
<div class="card" style="left:611px;top:1886px"><div class="ph" role="img" aria-label="White chew bone" style="background:radial-gradient(circle,#f4efe6,#ffffff)"></div><div class="new"><span>NEW</span></div><div class="icons"><i></i><i></i><i></i></div></div>
<div class="card" style="left:867px;top:1886px"><div class="ph" role="img" aria-label="Bowl of bone-shaped biscuits" style="background:radial-gradient(circle,#d99a5a,#f4e2c8)"></div><div class="icons"><i></i><i></i><i></i></div></div>
<div class="pinfo" style="left:97px;top:2164px"><h5>Expedita Distinctio</h5><p>$35.28</p><div class="stars">★★★★★</div></div>
<div class="pinfo" style="left:356px;top:2164px"><h5>Culpa Qui Officia</h5><p>$325.3</p><div class="stars">★★★★★</div></div>
<div class="pinfo" style="left:611px;top:2164px"><h5>Voluptatibus Maiores</h5><p>$52.28</p><div class="stars">★★★★★</div></div>
<div class="pinfo" style="left:867px;top:2164px"><h5>Omnis Dllendus</h5><p>$25.28</p><div class="stars">★★★★★</div></div>

<div class="card" style="left:97px;top:2295px"><div class="ph" role="img" aria-label="Blue bowl of kibble" style="background:radial-gradient(circle,#6a3a2a,#3a7fd0)"></div><div class="new"><span>NEW</span></div><div class="icons"><i></i><i></i><i></i></div></div>
<div class="card" style="left:356px;top:2295px"><div class="ph" role="img" aria-label="Black treat container" style="background:radial-gradient(circle,#3a3a3a,#e8e4dc)"></div><div class="icons"><i></i><i></i><i></i></div></div>
<div class="card" style="left:611px;top:2295px"><div class="ph" role="img" aria-label="Pile of meaty treats" style="background:radial-gradient(circle,#8a3a1a,#f0d8c0)"></div><div class="new"><span>NEW</span></div><div class="icons"><i></i><i></i><i></i></div></div>
<div class="card" style="left:867px;top:2295px"><div class="ph" role="img" aria-label="Bone-shaped cookies" style="background:radial-gradient(circle,#b07a4a,#f6ead8)"></div><div class="icons"><i></i><i></i><i></i></div></div>
<div class="pinfo" style="left:97px;top:2572px"><h5>Nam Liberotemp</h5><p>$35.28</p><div class="stars">★★★★★</div></div>
<div class="pinfo" style="left:356px;top:2572px"><h5>Maxime Placeat</h5><p>$325.3</p><div class="stars">★★★★★</div></div>
<div class="pinfo" style="left:611px;top:2572px"><h5>Doluus Maiores</h5><p>$52.28</p><div class="stars">★★★★★</div></div>
<div class="pinfo" style="left:867px;top:2572px"><h5>Serunt Mollit</h5><p>$25.28</p><div class="stars">★★★★★</div></div>

<section class="news-band" role="img" aria-label="Soft photo of a person hugging a dog"></section>
<div class="news-panel">
  <h3 class="news-title">Sign Up For Newsletter</h3>
  <p class="news-text">Get the latest treat drops, box previews and member deals sent straight to your inbox each month.</p>
  <div class="news-input">Enter Email..</div>
  <span class="btn news-btn">Subscribe</span>
</div>

<h2 class="sec-title" style="top:3112px">Our Blog Posts</h2>
<div class="abs" role="img" aria-label="Photo of a puppy holding a chew toy" style="left:903px;top:3050px;width:156px;height:158px;background:radial-gradient(circle,#e0b27a,#ffffff 70%)"></div>

<article class="post" style="left:97px"><div class="ph" role="img" aria-label="Photo of a bowl of dog food on wood" style="background:linear-gradient(120deg,#c48a5a,#7a4a2a)"></div><div class="body"><div class="date">▦ May 30,2017</div><h5>Excepteur Aecat Cupidatat</h5><p>Simple tips for choosing healthy snacks your dog will love, plus ways to keep treat time fun and balanced.</p><span class="more">Read More →</span></div></article>
<article class="post" style="left:442px"><div class="ph" role="img" aria-label="Photo of a woman holding a small dog" style="background:linear-gradient(120deg,#d8c8b8,#6a5a6a)"></div><div class="body"><div class="date">▦ May 30,2017</div><h5>Similique Sunt In Culpa Qui</h5><p>Meet the people behind each box and learn how we test every chew and biscuit before it ships out.</p><span class="more">Read More →</span></div></article>
<article class="post" style="left:783px"><div class="ph" role="img" aria-label="Photo of dogs at a kitchen table" style="background:linear-gradient(120deg,#a07a5a,#4a3a2a)"></div><div class="body"><div class="date">▦ May 30,2017</div><h5>Cum Soluta Nobis Est Eligendi</h5><p>Easy homemade treat ideas for rainy days, with simple recipes that use pantry basics and lots of love.</p><span class="more">Read More →</span></div></article>

<footer class="footer">
  <div class="fcol contact" style="left:97px;width:270px"><h6>Contact Us</h6>
    <ul><li><svg width="14" height="18" viewBox="0 0 14 18"><path d="M7 1a6 6 0 0 1 6 6c0 4-6 10-6 10S1 11 1 7a6 6 0 0 1 6-6z" fill="#ddd"/><circle cx="7" cy="7" r="2" fill="#1f1f1f"/></svg><span>Pup Snack Den subscription box<br>12 Barkley Lane, Suite 4<br>Springfield 00001</span></li>
    <li><svg width="14" height="14" viewBox="0 0 16 16"><path d="M3 1l3 3-2 2c1 2 3 4 5 5l2-2 3 3-2 3C7 15 1 9 1 3z" fill="#ddd"/></svg><span>Phone: (555) - 014 - 2290</span></li>
    <li><svg width="16" height="12" viewBox="0 0 16 12"><rect x="1" y="1" width="14" height="10" fill="none" stroke="#ddd" stroke-width="1.5"/><path d="M1 1l7 6 7-6" fill="none" stroke="#ddd" stroke-width="1.5"/></svg><span>Email: hello@pupsnackden.example</span></li></ul></div>
  <div class="fcol" style="left:403px"><h6>Quick Links</h6><ul><li>Home</li><li>About Us</li><li>Products</li><li>Blog</li><li>Contact US</li></ul></div>
  <div class="fcol" style="left:575px"><h6>Other Links</h6><ul><li>Policies</li><li>Orders</li><li>Return</li><li>Bulk Discount</li><li>Quality</li></ul></div>
  <div class="fcol" style="left:761px"><h6>My Account</h6><ul><li>subscription box</li><li>Information</li><li>Food Range</li><li>Box Weight</li><li>Voluptatibus</li></ul></div>
  <div class="fcol" style="left:939px"><h6>Stay Connected</h6><div class="social"><i></i><i></i><i></i><i></i></div></div>
  <div class="fbottom"><span>© copyright 2017 Pup Snack Den subscription box business. All rights reserved</span><div class="pay"><i></i><i></i><i></i><i></i><i></i></div></div>
</footer>

</body>
</html>
```